Bref créative
Business Cards and Stationary for IT Company
VarloxIQ Solutions Limited
Professional
Tarik Merola
Managing Director
718, Building 6
Hollow Crest,
Delta 9,
Greater Noida,
India
tmerola@varloxiq.example
www.varloxiq.example

```html
<!DOCTYPE html>
<html lang="en">
<head>
<meta charset="utf-8">
<title>VarloxIQ Business Cards</title>
<link href="https://fonts.googleapis.com/css2?family=Arimo:wght@400;700&display=swap" rel="stylesheet">
<style>
  :root {
    --backdrop: #3b3b3b;
    --card: #ffffff;
    --ink: #3a3a3a;
    --ink-soft: #666666;
    --brand-blue: #1d5fa8;
    --brand-orange: #f07a1a;
    --tab-blue: #2a6fc0;
    --tab-dark: #0f3c74;
    --rule: #c9c9c9;
  }
  * { box-sizing: border-box; margin: 0; padding: 0; }
  html, body { width: 1200px; height: 852px; overflow: hidden; }
  body {
    background: var(--backdrop);
    font-family: "Arimo", Arial, sans-serif;
    color: var(--ink);
    position: relative;
  }
  .card {
    position: absolute;
    width: 540px;
    height: 310px;
    background: var(--card);
    border-radius: 22px;
    overflow: hidden;
  }
  .card--front { left: 60px; top: 90px; }
  .card--alt { left: 600px; top: 452px; }

  .edge-tab {
    position: absolute;
    width: 10px;
    height: 90px;
    background: linear-gradient(90deg, var(--tab-dark), var(--tab-blue));
  }
  .edge-tab--right { right: 0; border-radius: 6px 0 0 6px; }
  .edge-tab--left { left: 0; border-radius: 0 6px 6px 0; background: linear-gradient(270deg, var(--tab-dark), var(--tab-blue)); }

  .brand {
    position: absolute;
    display: flex;
    align-items: center;
    gap: 12px;
  }
  .brand-mark {
    border-radius: 50%;
    background: var(--brand-orange);
    flex: none;
  }
  .brand-name {
    font-weight: 400;
    color: var(--ink);
    line-height: 1;
    letter-spacing: -0.5px;
  }

  .card--front .brand { left: 128px; top: 68px; }
  .card--front .brand-mark { width: 62px; height: 62px; }
  .card--front .brand-name { font-size: 48px; }

  .card--alt .brand { left: 48px; top: 180px; }
  .card--alt .brand-mark { width: 48px; height: 48px; }
  .card--alt .brand-name { font-size: 38px; }

  .person-name { color: var(--brand-blue); font-weight: 700; font-size: 17px; }
  .person-title { font-weight: 700; font-size: 12px; color: var(--ink); margin-top: 4px; }

  .card--front .person { position: absolute; right: 300px; top: 206px; text-align: right; }
  .card--alt .person { position: absolute; left: 312px; top: 44px; }

  .contact {
    position: absolute;
    border-left: 1px solid var(--rule);
    padding-left: 12px;
    font-size: 11.5px;
    line-height: 1.35;
    color: var(--ink-soft);
  }
  .card--front .contact { left: 262px; top: 176px; }
  .card--alt .contact { left: 300px; top: 94px; }

  .address { margin-bottom: 12px; }
  .contact-row { display: flex; align-items: center; gap: 7px; margin-top: 3px; }
  .contact-row svg { width: 12px; height: 12px; flex: none; }
</style>
</head>
<body>

<article class="card card--front">
  <span class="edge-tab edge-tab--right" style="top:112px"></span>
  <div class="brand">
    <span class="brand-mark"></span>
    <span class="brand-name">VarloxIQ</span>
  </div>
  <div class="person">
    <p class="person-name">Tarik Merola</p>
    <p class="person-title">Managing Director</p>
  </div>
  <div class="contact">
    <p class="address">718, Building 6<br>Hollow Crest, Delta 9,<br>Greater Noida, India</p>
    <p class="contact-row">
      <svg viewBox="0 0 12 12" aria-hidden="true"><rect x="3" y="0.5" width="6" height="11" rx="1.2" fill="none" stroke="#1d5fa8" stroke-width="1.2"/><circle cx="6" cy="9.5" r="0.8" fill="#1d5fa8"/></svg>
      +919812340076
    </p>
    <p class="contact-row">
      <svg viewBox="0 0 12 12" aria-hidden="true"><rect x="0.5" y="2.5" width="11" height="7" fill="none" stroke="#1d5fa8" stroke-width="1.2"/><path d="M0.5 2.5 L6 7 L11.5 2.5" fill="none" stroke="#1d5fa8" stroke-width="1.2"/></svg>
      tmerola@varloxiq.example
    </p>
  </div>
</article>

<article class="card card--alt">
  <span class="edge-tab edge-tab--left" style="top:162px"></span>
  <span class="edge-tab edge-tab--right" style="top:24px"></span>
  <div class="person">
    <p class="person-name">Tarik Merola</p>
    <p class="person-title">Managing Director</p>
  </div>
  <div class="contact">
    <p class="address">718, Building 6<br>Hollow Crest, Delta 9,<br>Greater Noida, India</p>
    <p class="contact-row">
      <svg viewBox="0 0 12 12" aria-hidden="true"><rect x="3" y="0.5" width="6" height="11" rx="1.2" fill="none" stroke="#1d5fa8" stroke-width="1.2"/><circle cx="6" cy="9.5" r="0.8" fill="#1d5fa8"/></svg>
      +919812340076
    </p>
    <p class="contact-row">
      <svg viewBox="0 0 12 12" aria-hidden="true"><rect x="0.5" y="2.5" width="11" height="7" fill="none" stroke="#1d5fa8" stroke-width="1.2"/><path d="M0.5 2.5 L6 7 L11.5 2.5" fill="none" stroke="#1d5fa8" stroke-width="1.2"/></svg>
      tmerola@varloxiq.example
    </p>
    <p class="contact-row">
      <svg viewBox="0 0 12 12" aria-hidden="true"><circle cx="6" cy="6" r="5.2" fill="none" stroke="#1d5fa8" stroke-width="1.1"/><ellipse cx="6" cy="6" rx="2.3" ry="5.2" fill="none" stroke="#1d5fa8" stroke-width="1"/><path d="M0.8 6 H11.2" stroke="#1d5fa8" stroke-width="1"/></svg>
      www.varloxiq.example
    </p>
  </div>
  <div class="brand">
    <span class="brand-mark"></span>
    <span class="brand-name">VarloxIQ</span>
  </div>
</article>

</body>
</html>
```